Business card for Chiropractic clinics needs reworked / redesigned

The business card in attachment was designed 10 years ago. It is in need of an update.
We have 2 clinics:
VELDHOVE KLINIEK & VELDHOVE KLINIEK NOORD
Only one address needs to be on the card for doctors that only work in one clinic and two addresses need to be on the card for the doctors that work in both clinics.

Target Market(s)

patients/referrers

Industry/Entity Type

Medical

Contact Information for Business Card

Logo (in full or zoomed-in)
Clinic Name
Doctor name and title
clinic address, website, tel, email

Font styles to use
Sans Serif

Colors

Designer to choose colors to be used in the design.

Requirements
Must have
• Good contrast/readability
• We like modern minimalistic designs
• The Bcard needs to project our very high standard of proficiency/professionalism
Should not have
• Not curly
• Not to much colours

```html
<!DOCTYPE html>
<html lang="nl">
<head>
<meta charset="utf-8">
<title>Veldhove Kliniek – visitekaartje</title>
<link href="https://fonts.googleapis.com/css2?family=Oswald:wght@500;600&family=Source+Sans+3:wght@400;600;700&display=swap" rel="stylesheet">
<style>
  :root {
    --clinic-green: #053a28;
    --paper-white: #ffffff;
    --ink-dark: #1d2a24;
    --backdrop: #e9e6e1;
    --card-shadow: rgba(0, 0, 0, 0.18);
  }
  * { box-sizing: border-box; margin: 0; padding: 0; }
  html, body {
    width: 1200px;
    height: 800px;
    overflow: hidden;
    background: var(--backdrop);
  }
  .canvas {
    width: 1200px;
    height: 800px;
    display: flex;
    align-items: center;
    justify-content: center;
    gap: 90px;
  }
  .card {
    position: relative;
    width: 330px;
    height: 510px;
    background: var(--clinic-green);
    box-shadow: 0 14px 30px var(--card-shadow);
    color: var(--paper-white);
    overflow: hidden;
  }

  /* Front */
  .brand-block {
    position: absolute;
    left: 44px;
    right: 30px;
    bottom: 64px;
    display: flex;
    align-items: flex-end;
    gap: 14px;
  }
  .brand-dot {
    width: 16px;
    height: 16px;
    border-radius: 50%;
    background: var(--paper-white);
    flex: none;
    margin-bottom: 10px;
  }
  .brand-name {
    font-family: "Oswald", sans-serif;
    font-weight: 600;
    font-size: 42px;
    line-height: 1.02;
    letter-spacing: 0.5px;
    text-transform: uppercase;
    color: var(--paper-white);
  }

  /* Back */
  .doctor-panel {
    position: absolute;
    top: 16px;
    left: 0;
    right: 16px;
    height: 150px;
    background: var(--paper-white);
    border-bottom-left-radius: 34px;
    color: var(--ink-dark);
    padding: 34px 24px 0 26px;
    font-family: "Source Sans 3", sans-serif;
  }
  .doctor-name {
    font-weight: 700;
    font-size: 21px;
    letter-spacing: 0.2px;
  }
  .doctor-title {
    font-weight: 600;
    font-size: 14px;
    letter-spacing: 1.2px;
    margin-top: 6px;
  }
  .doctor-phone {
    font-size: 15px;
    margin-top: 3px;
  }
  .clinic-list {
    position: absolute;
    left: 26px;
    right: 20px;
    top: 220px;
    display: flex;
    flex-direction: column;
    gap: 46px;
  }
  .clinic {
    font-style: normal;
  }
  .clinic-name {
    font-family: "Oswald", sans-serif;
    font-weight: 500;
    font-size: 20px;
    text-transform: uppercase;
    letter-spacing: 0.3px;
    margin-bottom: 6px;
  }
  .clinic-line {
    font-family: "Source Sans 3", sans-serif;
    font-weight: 400;
    font-size: 14px;
    line-height: 1.45;
  }
</style>
</head>
<body>
<main class="canvas">
  <section class="card card-front" aria-label="Voorzijde visitekaartje">
    <div class="brand-block">
      <span class="brand-dot"></span>
      <p class="brand-name">Veldhove<br>Kliniek</p>
    </div>
  </section>

  <section class="card card-back" aria-label="Achterzijde visitekaartje">
    <div class="doctor-panel">
      <p class="doctor-name">Pieter VANLAERE D.C.</p>
      <p class="doctor-title">CHIROPRACTOR</p>
      <p class="doctor-phone">0.112.23.44.555</p>
    </div>

    <div class="clinic-list">
      <address class="clinic">
        <p class="clinic-name">Veldhove Kliniek</p>
        <p class="clinic-line">Lindenlaan 14</p>
        <p class="clinic-line">+32 (0) 9 000 12 34</p>
        <p class="clinic-line">info@veldhovekliniek.be</p>
        <p class="clinic-line">www.veldhovekliniek.be</p>
      </address>
      <address class="clinic">
        <p class="clinic-name">Veldhove Kliniek Noord</p>
        <p class="clinic-line">Molenstraat 7</p>
        <p class="clinic-line">+32 (0) 9 000 56 78</p>
        <p class="clinic-line">www.veldhovekliniek-noord.be</p>
      </address>
    </div>
  </section>
</main>
</body>
</html>
```